Business Card Design

Printing and photocopying solutions, computer sales, photocopier sales and service, stationery needs

We aim to be the best for reliability, knowledge, skilled technical ability and highly ethical in business dealings. We would like to present as professional and the key person for dealing with for all customers. We are based in the Solomon Islands and therefore part of a developing country where many services and infrastructures are not in place. We would like to be seen as leading the field with technology and advanced office support. We strongly support the community and education systems with our current services and are seeking to expand the reach to encompass other service offerings

Target Market(s)

Business, Schools, Government offices, Churches, Non-government organisations

Industry/Entity Type

Business

Contact Information for Business Card

Harbourline Print
harbourlineprint@mailbay.net
+677 7418902 +677 8257113
PO Box 9
Auki, Malaita Province
Solomon Islands

Requirements
Must have
• professional appearance. Some Blue colouring
Must have easy to read phone number so required the phone number to be large font

Must have Shop address as well
Shop 7, Tidewell Building
Auki, Malaita, Solomon Islands
Nice to have
• Keep simple and professional with appearance of the business card styles, use the back of the card for Logo and a list of the basic services that is offered from Harbourline Print

```html
<!DOCTYPE html>
<html lang="en">
<head>
<meta charset="utf-8">
<title>Harbourline Print – Business Card</title>
<link href="https://fonts.googleapis.com/css2?family=Exo+2:wght@400;500;700;800&display=swap" rel="stylesheet">
<style>
  :root {
    --blue-deep: #1f63c4;
    --blue-mid: #2a86dc;
    --blue-light: #3aa2ee;
    --paper: #e9ebee;
    --paper-edge: #f5f6f8;
    --ink: #111318;
    --white: #ffffff;
    --backdrop: #d9dce1;
  }
  * { margin: 0; padding: 0; box-sizing: border-box; }
  html, body {
    width: 1200px; height: 1019px; overflow: hidden;
    background: var(--backdrop);
    font-family: "Exo 2", sans-serif;
  }
  .stage {
    width: 1200px; height: 1019px;
    display: flex; flex-direction: column; align-items: center; justify-content: center;
    gap: 50px;
  }
  .card {
    width: 720px; height: 412px;
    position: relative; overflow: hidden;
    background: var(--paper-edge);
    box-shadow: 0 6px 18px rgba(0,0,0,.18);
  }
  /* front */
  .front__blue-side {
    position: absolute; left: 0; top: 0; width: 360px; height: 100%;
    background: linear-gradient(160deg, var(--blue-light), var(--blue-deep));
  }
  .front__identity {
    position: absolute; left: 36px; top: 0; width: 324px; height: 376px;
    background: var(--paper);
  }
  .front__contact {
    position: absolute; left: 360px; top: 36px; width: 324px; height: 240px;
    background: linear-gradient(160deg, var(--blue-light), var(--blue-deep));
  }
  .logo {
    position: absolute; left: 34px; top: 60px;
    padding: 10px 22px;
    background: var(--blue-deep);
    border-radius: 8px;
    color: var(--white);
    font-size: 26px; font-weight: 500; letter-spacing: .5px;
  }
  .person { position: absolute; left: 34px; bottom: 40px; color: var(--ink); }
  .person__name { font-size: 26px; font-weight: 800; letter-spacing: 1px; }
  .person__role { font-size: 17px; font-weight: 500; margin-top: 2px; }
  .contact-list {
    list-style: none;
    position: absolute; left: 28px; top: 30px;
    color: var(--white); font-size: 15px; line-height: 1.35;
  }
  .contact-list li { display: flex; align-items: flex-start; gap: 10px; margin-bottom: 8px; }
  .contact-list svg { flex: none; width: 14px; height: 14px; margin-top: 3px; fill: var(--white); }
  .contact-list .phone { font-size: 18px; font-weight: 700; }
  /* back */
  .back { background: var(--paper-edge); }
  .back__field {
    position: absolute; inset: 40px;
    background: radial-gradient(circle at 50% 55%, var(--blue-light), var(--blue-deep) 75%);
  }
</style>
</head>
<body>
<main class="stage">
  <section class="card front" aria-label="Card front">
    <div class="front__blue-side"></div>
    <div class="front__identity">
      <div class="logo">Harbourline Print</div>
      <div class="person">
        <div class="person__name">DANIEL KEREWA</div>
        <div class="person__role">Managing Director</div>
      </div>
    </div>
    <div class="front__contact">
      <ul class="contact-list">
        <li>
          <svg viewBox="0 0 14 14"><path d="M7 0a5 5 0 0 0-5 5c0 3.6 5 9 5 9s5-5.4 5-9a5 5 0 0 0-5-5zm0 7a2 2 0 1 1 0-4 2 2 0 0 1 0 4z"/></svg>
          <span>Shop 7, Tidewell Building<br>Auki, Malaita</span>
        </li>
        <li class="phone">
          <svg viewBox="0 0 14 14"><path d="M3 0l2.5 3-1.5 1.8a8 8 0 0 0 5.2 5.2L11 8.5 14 11l-1.8 2.4C6 13.5.5 8 .6 1.8z"/></svg>
          <span>+677 7418902</span>
        </li>
        <li class="phone">
          <svg viewBox="0 0 14 14"><rect x="3" y="0" width="8" height="14" rx="1.5"/><rect x="4.5" y="1.8" width="5" height="8.5" fill="#2a86dc"/></svg>
          <span>+677 8257113</span>
        </li>
        <li>
          <svg viewBox="0 0 14 14"><rect x="0" y="2" width="14" height="10" rx="1"/><path d="M0.8 3l6.2 4.5L13.2 3" stroke="#2a86dc" stroke-width="1.3" fill="none"/></svg>
          <span>harbourlineprint@mailbay.net</span>
        </li>
        <li>
          <svg viewBox="0 0 14 14"><circle cx="7" cy="7" r="6.3" fill="none" stroke="#fff" stroke-width="1.3"/><path d="M.7 7h12.6M7 .7c-3 3.5-3 9.1 0 12.6M7 .7c3 3.5 3 9.1 0 12.6" stroke="#fff" stroke-width="1.1" fill="none"/></svg>
          <span>www.harbourlineprint.sb</span>
        </li>
      </ul>
    </div>
  </section>

  <section class="card back" aria-label="Card back">
    <div class="back__field"></div>
  </section>
</main>
</body>
</html>
```